Brick pressure cleaning business needs business cards that are memorable

The business is called Kestrel hydroblast brick and pressure cleaning.
we Kestrel Hydroblast on new houses and driveways. I would like a logo with water spraying out of the letter s in the wording. Also bricks on the card somehow and maybe the word kestrel to be on an angle above the rest of the business name if possible. some shinny gold would be nice somewhere to. Would like to list our services on the back of card- red and cream brick clean, green stain removal, floor scrapes, fence panel clean or changeout. Driveway cleans. hard surface pressure cleans.

Target Market(s)

Building companies and home reno people

Industry/Entity Type

construction

Contact Information for Business Card

business name,phone,number my name, services on the back

Colors
0054AA
0677BA
7BADD7
CADEEF
E8F1F8
FFF300
FFF600
FEFA6F
FFFEC7
FFFEE8

```html
<!DOCTYPE html>
<html lang="en">
<head>
<meta charset="utf-8">
<title>Kestrel Hydroblast – Business Card</title>
<link href="https://fonts.googleapis.com/css2?family=Josefin+Sans:wght@300&family=Montserrat:wght@400;600;700&display=swap" rel="stylesheet">
<style>
  :root {
    --page: #d9d9d9;
    --card-white: #ffffff;
    --brand-red: #bf1e2e;
    --ink: #111111;
    --cream: #fdf6dc;
    --faint-mark: #d0574b;
    --service-text: #f6e4da;
  }
  * { box-sizing: border-box; margin: 0; padding: 0; }
  html, body {
    width: 1200px; height: 1200px; overflow: hidden;
    background: var(--page);
    font-family: "Montserrat", Arial, sans-serif;
  }
  .card {
    position: absolute; left: 150px; width: 898px; height: 525px;
    box-shadow: 0 2px 6px rgba(0,0,0,.25);
    overflow: hidden;
  }
  .card--front { top: 56px; background: var(--card-white); }
  .card--back { top: 616px; background: var(--brand-red); }

  .front__bar {
    position: absolute; left: 777px; top: 0; width: 26px; height: 219px;
    background: var(--brand-red);
  }
  .front__wordmark {
    position: absolute; left: 82px; top: 96px;
    font-weight: 700; font-size: 66px; line-height: 1.05;
    color: var(--ink); letter-spacing: -1px;
  }
  .front__name {
    position: absolute; right: 95px; top: 280px;
    font-weight: 700; font-size: 30px; color: var(--ink);
  }
  .front__name .surname { color: var(--brand-red); }
  .contact {
    position: absolute; right: 95px; top: 342px;
    list-style: none; text-align: right;
  }
  .contact li {
    display: flex; justify-content: flex-end; align-items: center;
    height: 35px; font-size: 21px; color: var(--ink);
  }
  .contact svg { width: 13px; height: 13px; margin-left: 12px; fill: var(--brand-red); }
  .front__rule {
    position: absolute; left: 78px; top: 443px; width: 410px; height: 3px;
    background: var(--brand-red);
  }

  .back__bar {
    position: absolute; left: 68px; top: 0; width: 22px; height: 203px;
    background: var(--cream);
  }
  .back__mark {
    position: absolute; left: 420px; top: 80px;
    font-weight: 700; font-size: 66px; line-height: 1.05;
    color: var(--faint-mark); letter-spacing: -1px;
  }
  .services {
    position: absolute; left: 68px; top: 236px; list-style: none;
    font-family: "Josefin Sans", Arial, sans-serif; font-weight: 300;
    font-size: 27px; color: var(--service-text);
  }
  .services li { height: 41.5px; }
  .services li::before { content: "•"; margin-right: 8px; font-size: 20px; vertical-align: 3px; }
</style>
</head>
<body>
  <section class="card card--front">
    <div class="front__bar"></div>
    <div class="front__wordmark">Kestrel<br>Hydroblast</div>
    <p class="front__name">Dale <span class="surname">Merrow</span></p>
    <ul class="contact">
      <li>555-014-2270
        <svg viewBox="0 0 24 24" aria-hidden="true"><path d="M6.6 10.8a15 15 0 0 0 6.6 6.6l2.2-2.2c.3-.3.7-.4 1-.2 1.1.4 2.3.6 3.6.6.6 0 1 .4 1 1V20c0 .6-.4 1-1 1A17 17 0 0 1 3 4c0-.6.4-1 1-1h3.5c.6 0 1 .4 1 1 0 1.3.2 2.5.6 3.6.1.3 0 .7-.2 1z"/></svg>
      </li>
      <li>hello@kestrelhb.com
        <svg viewBox="0 0 24 24" aria-hidden="true"><path d="M2 5h20v14H2z M2 5l10 8 10-8" stroke="#fff" stroke-width="1.5"/></svg>
      </li>
      <li>www.kestrelhb.com
        <svg viewBox="0 0 24 24" aria-hidden="true"><circle cx="12" cy="12" r="10"/><path d="M2 12h20M12 2c3 3 3 17 0 20M12 2c-3 3-3 17 0 20" stroke="#fff" stroke-width="1.4" fill="none"/></svg>
      </li>
    </ul>
    <div class="front__rule"></div>
  </section>

  <section class="card card--back">
    <div class="back__bar"></div>
    <div class="back__mark" aria-hidden="true">Kestrel<br>Hydroblast</div>
    <ul class="services">
      <li>Brick Clean</li>
      <li>Green Stain Removal</li>
      <li>Floor Scrapes</li>
      <li>Fence Panel Clean or Changeout</li>
      <li>Driveway Cleans</li>
      <li>Hard Surface Pressure Cleans</li>
    </ul>
  </section>
</body>
</html>
```